Corvane Brochure

I would like to update our brochure and add additional services as well as change our logo, We are a full service PEO and a full service Payroll company
Target Market(s)
Business to Business
Industry/Entity Type
Payroll and Benefits
Font styles to use
Sans Serif

```html
<!DOCTYPE html>
<html lang="en">
<head>
<meta charset="utf-8">
<title>Corvane Brochure – HR Services</title>
<link rel="stylesheet" href="https://fonts.googleapis.com/css2?family=Lora:wght@400;500&family=Open+Sans:wght@400;600;700&display=swap">
<style>
  :root {
    --accent: #e8731e;
    --ink: #1f2733;
    --heading: #1e2a40;
    --paper: #ffffff;
  }
  * { box-sizing: border-box; margin: 0; padding: 0; }
  html, body { width: 849px; height: 1200px; overflow: hidden; background: var(--paper); }
  .page {
    position: relative; width: 849px; height: 1200px;
    font-family: "Open Sans", Arial, sans-serif; color: var(--ink);
    font-size: 11.4px; line-height: 14.2px;
  }
  .service { position: absolute; }
  .col-left { left: 40px; width: 345px; }
  .col-right { left: 440px; width: 372px; }
  .service-head { display: flex; align-items: center; gap: 12px; margin-bottom: 8px; }
  .icon { flex: 0 0 54px; width: 54px; height: 54px; }
  .service-title {
    font-family: "Lora", Georgia, serif; font-weight: 400;
    font-size: 20px; line-height: 23px; color: var(--heading);
  }
  .pricing { margin-bottom: 12px; }
  .pricing.indent { padding-left: 66px; margin-top: -4px; }
  .pricing p { margin: 0; }
  .pricing b { font-weight: 700; }
  .body-text p { margin-bottom: 12px; }
  .body-text ul { margin: -9px 0 12px 34px; }
  .body-text li { margin: 0; }
</style>
</head>
<body>
<div class="page">

  <section class="service col-left" style="top:22px">
    <div class="service-head">
      <svg class="icon" viewBox="0 0 56 56" aria-hidden="true">
        <rect width="56" height="56" rx="4" fill="var(--accent)"/>
        <path d="M14 16 h12 q2 0 2 2 v24 q0-2-2-2 h-12z M42 16 h-12 q-2 0-2 2 v24 q0-2 2-2 h12z" fill="none" stroke="#fff" stroke-width="2.4" stroke-linejoin="round"/>
      </svg>
      <h2 class="service-title">Custom Employee Handbooks</h2>
    </div>
    <div class="pricing indent">
      <p><b>Single State:</b></p>
      <p>1-9 Emp's: $349</p>
      <p>10-24 Emp's: $479</p>
      <p>25-74 Emp's: $695</p>
      <p>75+ Emp's: Quote</p>
      <p><b>Additional States:</b></p>
      <p>Per State: $149</p>
      <p>California: $195 (Additional)</p>
    </div>
    <div class="body-text">
      <p>A comprehensive employee handbook will lessen the potential of misunderstandings, keep employees informed and mitigate the risk of litigation.</p>
      <p>Your assigned HR professional will ensure that your employee handbook covers all the bases, including, but not limited to:</p>
      <ul>
        <li>Employment status</li>
        <li>Attendance</li>
        <li>Records retention</li>
        <li>Benefits</li>
        <li>Payroll</li>
        <li>Standards of conduct</li>
        <li>Hours</li>
        <li>Leaves of absence</li>
        <li>Conduct and disciplinary actions</li>
      </ul>
      <p>Corvane can draft a new handbook or review a current one and revise as needed.</p>
    </div>
  </section>

  <section class="service col-left" style="top:458px">
    <div class="service-head">
      <svg class="icon" viewBox="0 0 56 56" aria-hidden="true">
        <rect width="56" height="56" rx="4" fill="var(--accent)"/>
        <circle cx="21" cy="22" r="5" fill="#fff"/>
        <circle cx="36" cy="22" r="5" fill="#fff"/>
        <path d="M12 40 q0-10 9-10 q9 0 9 10z M27 40 q0-10 9-10 q9 0 9 10z" fill="#fff"/>
      </svg>
      <h2 class="service-title">Coaching &amp; Problem Solving</h2>
    </div>
    <div class="pricing indent">
      <p><b>Per Hour:</b> $95 (minimum 3 hours)</p>
      <p><b>Each Additional Hour:</b> $79</p>
    </div>
    <div class="body-text">
      <p>As requested, your dedicated HR Professional provides support to you and your management team, to navigate and resolve any type of employee matter in a timely manner, focusing on resolving each matter fairly, legally and in the best interest of the business.</p>
    </div>
  </section>

  <section class="service col-left" style="top:690px">
    <div class="service-head">
      <svg class="icon" viewBox="0 0 56 56" aria-hidden="true">
        <rect width="56" height="56" rx="4" fill="var(--accent)"/>
        <rect x="17" y="13" width="22" height="30" rx="2" fill="none" stroke="#fff" stroke-width="2.4"/>
        <path d="M22 21 h12 M22 27 h12 M22 33 h8" stroke="#fff" stroke-width="2.4"/>
      </svg>
      <h2 class="service-title">Job Descriptions</h2>
    </div>
    <div class="pricing indent">
      <p><b>Per Job Description</b></p>
      <p><b>1:</b> $139</p>
      <p><b>2 - 5:</b> $119 each</p>
      <p><b>6+:</b> $99 each</p>
    </div>
    <div class="body-text">
      <p>In order for there to be successful employee performance, it is critical to start with well-written job descriptions that accurately identify position duties, scope of authority, skills, competencies, education, training, experience, and physical requirements which support the organization's needs.</p>
      <p>Job descriptions are also key during the interviewing process to ensure that interview questions are relevant to the position, and selection criteria is consistent for each applicant.</p>
    </div>
  </section>

  <section class="service col-right" style="top:22px">
    <div class="service-head">
      <svg class="icon" viewBox="0 0 56 56" aria-hidden="true">
        <rect width="56" height="56" rx="4" fill="var(--accent)"/>
        <path d="M12 15 h22 v14 h-13 l-6 5 v-5 h-3z" fill="#fff"/>
        <path d="M38 23 h7 v13 h-3 v5 l-6-5 h-11 v-4 h13z" fill="#fff"/>
      </svg>
      <h2 class="service-title">Employee Counseling and Disciplinary Actions</h2>
    </div>
    <div class="pricing indent">
      <p><b>Per Hour:</b> $95 (minimum 3 hours)</p>
      <p><b>Each Additional Hour:</b> $79</p>
    </div>
    <div class="body-text">
      <p>It's an unfortunate necessity in doing business, fraught with potential pitfalls. Although the goal is to improve the problem area(s), we can help you minimize risks and draft supporting documentation to clearly describe the particulars of each situation in a manner that will remain in compliance with applicable laws and provide documentation that will clearly communicate the details of the issue(s) addressed and the steps taken by the company to rectify them should an employee file a complaint with the Department of Labor, EEOC or Division of Human Rights.</p>
    </div>
  </section>

  <section class="service col-right" style="top:410px">
    <div class="service-head">
      <svg class="icon" viewBox="0 0 56 56" aria-hidden="true">
        <rect width="56" height="56" rx="4" fill="var(--accent)"/>
        <rect x="12" y="14" width="32" height="20" rx="1" fill="none" stroke="#fff" stroke-width="2.4"/>
        <path d="M28 34 v8 M20 44 l8-10 l8 10" stroke="#fff" stroke-width="2.4" fill="none"/>
      </svg>
      <h2 class="service-title">Management and Employee Training</h2>
    </div>
    <div class="pricing indent">
      <p><b>Quoted per Session</b></p>
    </div>
    <div class="body-text">
      <p>Our professionally certified trainers incorporate best practices for employee relations, employment decisions and legal compliance into every training program we offer. We give your managers and supervisors the skills and knowledge to resolve difficult HR issues while limiting your exposure to costly litigation. We design our training programs to meet your specific needs, and all can be conducted on-site or virtually. State mandated sexual harassment prevention training is also available. Training sessions cost are quoted on a case-by-case basis.</p>
    </div>
  </section>

  <section class="service col-right" style="top:706px">
    <div class="service-head">
      <svg class="icon" viewBox="0 0 56 56" aria-hidden="true">
        <rect width="56" height="56" rx="4" fill="var(--accent)"/>
        <rect x="16" y="12" width="24" height="32" rx="1" fill="none" stroke="#fff" stroke-width="2.4"/>
        <path d="M21 20 h14 M21 26 h14 M21 32 h14 M21 38 h9" stroke="#fff" stroke-width="2"/>
      </svg>
      <h2 class="service-title">Labor Law Posters Program</h2>
    </div>
    <div class="pricing indent">
      <p><b>Monthly</b></p>
      <p><b>Single State:</b> $9</p>
      <p><b>Multiple States:</b> $15</p>
    </div>
    <div class="body-text">
      <p>Receive up-to-date, mandatory, printed or electronic posters for display in your workplace.</p>
    </div>
  </section>

  <section class="service col-right" style="top:848px">
    <div class="service-head">
      <svg class="icon" viewBox="0 0 56 56" aria-hidden="true">
        <rect width="56" height="56" rx="4" fill="var(--accent)"/>
        <path d="M28 11 l14 6 v10 q0 12-14 18 q-14-6-14-18 v-10z" fill="none" stroke="#fff" stroke-width="2.4" stroke-linejoin="round"/>
        <path d="M22 28 l4 4 l8-8" fill="none" stroke="#fff" stroke-width="2.4"/>
      </svg>
      <h2 class="service-title">Sexual Harassment Prevention Training</h2>
    </div>
    <div class="pricing indent">
      <p><b>Per Person Rate: $15.00</b></p>
    </div>
    <div class="body-text">
      <p>The training is conveniently conducted on-line so you can schedule it based on your own business demands. The training meets the mandated requirements under NYS and NYC law and can be used in all states except California which requires additional topics to cover. Corvane also can provide training to meet California requirements.</p>
    </div>
  </section>

</div>
</body>
</html>
```